Tax Firm - Creative Print Ads to Build New Clients

I'm the marketing director of an integrated financial services business based in Melbourne Australia. I need to create a series of 4 press ads to run in the local business newspaper.

Each ad needs to stand alone, but at the same time should appear visually as from the same company and be part of a series.

The ad will will 115mm by 255mm (1/3 of a page horizontal)

Final artwork needs to be setup using CMYK and at the exact dimensions no bleed.

Brief
- Our tax practice provides services to individuals & small businesses (cafes, tradespeoeple, retailers)
- Our tagline is Bold, Proactive, Strategic, Practical financial advice, Where Futures Settle (a brand logo will be provided)
- The company logo needs to be included
- Web address included
- phone number included
- The ad needs to be professional, yet energetic
- Stock photography should be at an absolute minimum where models are not identifable
- Graphics are prefered over stock images
- Sketches are great
- Key message - we do tax returns, we care about you as an individual, we've been in the Docklands for 20 years, we are your local partner in your financial journey
Updates

Target Market(s)

Individuals earning between 50,000 and 200,000 per annum

Industry/Entity Type

Accounting

Font styles to use
Sans Serif
Script

Colors
3176b5
1b1b1b
fbf289
ec1f27
85acd3
0355a3

Requirements
Must have
• Sell t services to individuals as primary audience, with small businesses as a secondary audience.
• ---- Updated ----
• The company is www.velmorbay.com.au
• I've added
• - logos (vertical, horizontal, reverse and our brand tagline too)
• - Brand Guidelines
Nice to have
• I want to see some graphics that sell the idea that we are a local firm with 20 years experience in the area.
• We care about individuals first
Should not have
• Avoid using stock images where the pretty model is identifiable, we hate to see actors in our ads

```html
<!DOCTYPE html>
<html lang="en">
<head>
<meta charset="utf-8">
<title>Velmor Bay – Tax Returns Press Ad</title>
<link rel="stylesheet" href="https://fonts.googleapis.com/css2?family=Open+Sans:wght@400;600;700&family=Allura&display=swap">
<style>
  :root {
    --paper: #f6f8f7;
    --sky: #85acd3;
    --ink: #1b1b1b;
    --sun: #fbf289;
    --signal: #ec1f27;
    --white: #ffffff;
    --stage: #e9e9e9;
  }
  * { box-sizing: border-box; margin: 0; padding: 0; }
  html, body {
    width: 1200px; height: 635px; overflow: hidden;
    background: var(--stage);
    font-family: "Open Sans", Arial, sans-serif;
  }
  .ad {
    position: absolute; left: 0; top: 47px;
    width: 1200px; height: 541px;
    background: var(--paper);
    overflow: hidden;
  }
  .gear-artwork {
    position: absolute; left: 83px; top: 55px;
    width: 395px; height: 370px;
    border-radius: 12px;
    background: linear-gradient(135deg, var(--signal) 0%, var(--signal) 45%, #3a3a3a 70%, var(--ink) 100%);
  }
  .service-list {
    position: absolute; left: 561px; top: 166px;
    list-style: none;
    color: var(--ink);
    font-size: 20px; line-height: 33px;
    text-transform: uppercase;
  }
  .service-list li { display: flex; align-items: center; gap: 10px; }
  .service-list svg { width: 18px; height: 18px; flex: none; }
  .brand-panel {
    position: absolute; left: 864px; top: 0;
    width: 336px; height: 443px;
    background: var(--sky);
    text-align: center;
    color: var(--ink);
  }
  .brand-name {
    position: absolute; left: 0; right: 0; top: 196px;
    font-size: 17px; font-weight: 400; letter-spacing: 5px;
  }
  .brand-message {
    position: absolute; left: 22px; right: 22px; top: 285px;
    font-size: 15px; line-height: 22px;
  }
  .accent-rule {
    position: absolute; left: 0; top: 443px;
    width: 1200px; height: 6px;
    background: var(--sun);
  }
  .tagline-band {
    position: absolute; left: 0; top: 449px;
    width: 864px; height: 92px;
    background: var(--sky);
  }
  .tagline {
    position: absolute; left: 30px; top: 10px;
    color: var(--white);
    font-size: 25px; font-weight: 600; letter-spacing: 4.5px;
    word-spacing: 12px;
  }
  .signature-line {
    position: absolute; left: 610px; top: 46px;
    color: var(--white);
    font-family: "Allura", cursive;
    font-size: 30px;
    transform: rotate(-4deg);
  }
  .contact-block {
    position: absolute; left: 864px; top: 449px;
    width: 336px; height: 92px;
    background: var(--ink);
    color: var(--white);
    text-align: center;
    font-size: 20px; line-height: 30px;
    padding-top: 16px;
  }
  .contact-block .phone { display: inline-flex; align-items: center; gap: 4px; }
  .contact-block svg { width: 16px; height: 16px; }
</style>
</head>
<body>
  <main class="ad">
    <div class="gear-artwork" role="img" aria-label="Interlocking gears illustration: a large red gear labelled Income meshing with black gears, one labelled Government"></div>

    <ul class="service-list">
      <li><svg viewBox="0 0 18 18"><rect x="1.5" y="2.5" width="13" height="13" rx="2" fill="none" stroke="#1b1b1b" stroke-width="1.6"/><path d="M5 9l3 3 8-9" fill="none" stroke="#1b1b1b" stroke-width="2"/></svg>Tax Returns</li>
      <li><svg viewBox="0 0 18 18"><rect x="1.5" y="2.5" width="13" height="13" rx="2" fill="none" stroke="#1b1b1b" stroke-width="1.6"/><path d="M5 9l3 3 8-9" fill="none" stroke="#1b1b1b" stroke-width="2"/></svg>Individuals</li>
      <li><svg viewBox="0 0 18 18"><rect x="1.5" y="2.5" width="13" height="13" rx="2" fill="none" stroke="#1b1b1b" stroke-width="1.6"/><path d="M5 9l3 3 8-9" fill="none" stroke="#1b1b1b" stroke-width="2"/></svg>Businesses</li>
      <li><svg viewBox="0 0 18 18"><rect x="1.5" y="2.5" width="13" height="13" rx="2" fill="none" stroke="#1b1b1b" stroke-width="1.6"/><path d="M5 9l3 3 8-9" fill="none" stroke="#1b1b1b" stroke-width="2"/></svg>Retailers</li>
      <li><svg viewBox="0 0 18 18"><rect x="1.5" y="2.5" width="13" height="13" rx="2" fill="none" stroke="#1b1b1b" stroke-width="1.6"/><path d="M5 9l3 3 8-9" fill="none" stroke="#1b1b1b" stroke-width="2"/></svg>Tradespeople</li>
    </ul>

    <aside class="brand-panel">
      <p class="brand-name">VELMOR BAY</p>
      <p class="brand-message">We do tax returns, we care about you as an individual, we've been in the Docklands for 20 years, we are your local partner in your financial journey</p>
    </aside>

    <div class="accent-rule"></div>

    <footer class="tagline-band">
      <p class="tagline">BOLD PROACTIVE STRATEGIC PRACTICAL</p>
      <p class="signature-line">Where Futures Settle</p>
    </footer>

    <div class="contact-block">
      <span class="phone"><svg viewBox="0 0 24 24"><path fill="#ffffff" d="M6.6 10.8a15.1 15.1 0 006.6 6.6l2.2-2.2a1 1 0 011-.25 11.4 11.4 0 003.6.57 1 1 0 011 1V20a1 1 0 01-1 1A17 17 0 013 4a1 1 0 011-1h3.5a1 1 0 011 1c0 1.25.2 2.45.57 3.57a1 1 0 01-.25 1z"/></svg>03 9555 0142</span><br>
      www.velmorbay.com.au
    </div>
  </main>
</body>
</html>
```